political campaign lawn sign - Governor's Council in Massachuesetts

We are looking for a political lawn sign. We are running a campaign for Governor's Council in Massachusetts. This sign will be on the lawn of homes and businesses so people driving by will see it. It needs to be simple and bold. The last name is long so maybe it could say vote for Marty and then Kolbeck will be big a bold on the next line??
We need it to say:
Vote for Martin Kolbeck
Governor's Council.

Target Market(s)

local residents

Industry/Entity Type

Politcal Campaign

Font styles to use
Sans Serif
Other font styles liked:
• not sure what font but a modern looking one such as Helvetica, Arial, Sans Seri, sharp sans..

Colors
0054AA
0677BA
7BADD7
CADEEF
E8F1F8
00AB8E
00BBA5
67D7C9
C6EFE9
E9F9F6
FFF300
FFF600
FEFA6F
FFFEC7
FFFEE8

Requirements
Must have
• My name written out with a Capital D and R but lower case for every other letter so its Marty Kolbeck
Nice to have
• modern font , the Colors of the lawn sign should have Blue, Yellow and White something bold that will stand out
Should not have
• any maps of Massachusetts

```html
<!DOCTYPE html>
<html lang="en">
<head>
<meta charset="utf-8">
<title>Vote for Marty Kolbeck – Lawn Sign</title>
<link rel="stylesheet" href="https://fonts.googleapis.com/css2?family=Montserrat:wght@500;600;800&display=swap">
<style>
  :root {
    --navy: #28396b;
    --yellow: #ffd503;
    --white: #ffffff;
    --ink: #111111;
    --backdrop: #333031;
  }
  html, body {
    margin: 0;
    padding: 0;
    width: 1200px;
    height: 1200px;
    overflow: hidden;
    background: var(--backdrop);
  }
  .lawn-sign {
    position: absolute;
    left: 40px;
    top: 180px;
    width: 1120px;
    height: 840px;
    display: block;
  }
  .sign-text { font-family: "Montserrat", sans-serif; }
  .headline { fill: var(--navy); font-weight: 500; font-size: 186px; }
  .first-name { fill: var(--white); font-weight: 600; font-size: 400px; }
  .last-name { fill: var(--white); font-weight: 800; font-size: 296px; }
  .office { fill: var(--ink); font-weight: 600; font-size: 88px; }
  .star { fill: var(--navy); }
</style>
</head>
<body>
<svg class="lawn-sign" viewBox="0 0 1544 1158" xmlns="http://www.w3.org/2000/svg" aria-label="Lawn sign: Vote for Marty Kolbeck, Governer's Council">
  <!-- yellow field -->
  <rect class="band-yellow" x="0" y="0" width="1544" height="1158" fill="var(--yellow)"/>

  <!-- white swoosh under the headline -->
  <path class="band-white" fill="var(--white)"
        d="M0 278 C 150 225, 480 190, 806 263 C 1020 300, 1300 320, 1544 260 L1544 1158 L0 1158 Z"/>

  <!-- navy body -->
  <path class="band-navy" fill="var(--navy)"
        d="M0 330 C 160 265, 480 230, 806 288 C 1050 328, 1330 345, 1544 260 L1544 1158 L0 1158 Z"/>

  <!-- yellow accent along the footer curve -->
  <path class="footer-accent" fill="var(--yellow)"
        d="M0 1004 L975 1002 C 1080 1004, 1200 1040, 1250 1080 C 1290 1110, 1300 1140, 1326 1158 L0 1158 Z"/>

  <!-- white footer panel -->
  <path class="footer-panel" fill="var(--white)"
        d="M0 1004 L960 1002 C 1060 1006, 1150 1030, 1200 1070 C 1250 1108, 1260 1140, 1296 1158 L0 1158 Z"/>

  <!-- headline -->
  <polygon class="star" transform="translate(227 118)"
           points="0,-50 13,-12 52,-11 21,12 32,49 0,27 -32,49 -21,12 -52,-11 -13,-12"/>
  <polygon class="star" transform="translate(1314 118)"
           points="0,-50 13,-12 52,-11 21,12 32,49 0,27 -32,49 -21,12 -52,-11 -13,-12"/>
  <text class="sign-text headline" x="772" y="185" text-anchor="middle" textLength="916" lengthAdjust="spacingAndGlyphs">VOTE FOR</text>

  <!-- candidate name -->
  <text class="sign-text first-name" x="772" y="640" text-anchor="middle">Marty</text>
  <text class="sign-text last-name" x="772" y="962" text-anchor="middle" letter-spacing="-6">Kolbeck</text>

  <!-- office -->
  <text class="sign-text office" x="60" y="1113" textLength="1006" lengthAdjust="spacingAndGlyphs">GOVERNER’S COUNCIL</text>
</svg>
</body>
</html>
```